Laser Cut Metal Property Sign Design

Take a previously completed logo design and modify it to be suitable for use in creating a laser cut metal property sign. Here is a link to the guidelines in order to have an acceptable design: https://www.plattenwerk-example.com/design-guidelines/. You previously did the logo design for Quiet Heron Farm which I’m uploading here as well. The overall size for the sign cannot exceed 1 meter x 1 meter but we will want it as big as possible. Also - underneath the oval logo you design, I would like to include the street address: 27841 Bravenfield Road. Is this a project that is possible?

```html
<!DOCTYPE html>
<html lang="en">
<head>
<meta charset="utf-8">
<title>Quiet Heron Farm – Property Sign Layout</title>
<link rel="stylesheet" href="https://fonts.googleapis.com/css2?family=Oswald:wght@700&family=Montserrat:wght@300;600&display=swap">
<style>
  :root {
    --ink: #1a1a1a;
    --paper: #ffffff;
    --guide: #c9c9c9;
    --guide-text: #6b5a5a;
    --art-fill: #d9d9d9;
  }
  html, body {
    margin: 0;
    padding: 0;
    width: 1200px;
    height: 1200px;
    overflow: hidden;
    background: var(--paper);
  }
  .canvas { display: block; width: 1200px; height: 1200px; }
  .sign-frame { fill: none; stroke: var(--ink); stroke-width: 5; stroke-linejoin: miter; }
  .corner-line { stroke: var(--ink); stroke-width: 5; }
  .corner-ornament { fill: var(--ink); }
  .farm-name {
    font-family: "Oswald", sans-serif;
    font-weight: 700;
    font-size: 64px;
    letter-spacing: 4px;
    fill: var(--ink);
  }
  .est-label, .town-label, .address-line {
    font-family: "Montserrat", sans-serif;
    font-weight: 600;
    fill: var(--ink);
  }
  .est-label { font-size: 30px; letter-spacing: 5px; }
  .town-label { font-size: 28px; letter-spacing: 10px; }
  .address-line { font-size: 38px; letter-spacing: 4px; }
  .illustration-area { fill: var(--art-fill); stroke: var(--ink); stroke-width: 6; }
  .cut-boundary { fill: none; stroke: var(--guide); stroke-width: 1; stroke-dasharray: 3 3; }
  .dimension-line { stroke: var(--guide); stroke-width: 1.5; fill: none; }
  .dimension-label {
    font-family: "Montserrat", sans-serif;
    font-weight: 300;
    font-size: 28px;
    fill: var(--guide-text);
  }
</style>
</head>
<body>
<svg class="canvas" viewBox="0 0 1200 1200" xmlns="http://www.w3.org/2000/svg">

  <!-- cut boundary (1 m × 1 m) -->
  <rect class="cut-boundary" x="150" y="150" width="840" height="840"/>

  <g class="sign" transform="translate(150 150)">
    <!-- frame with clipped corners -->
    <polygon class="sign-frame" points="159,45 681,45 795,159 795,681 681,795 159,795 45,681 45,159"/>

    <!-- corner extensions -->
    <line class="corner-line" x1="159" y1="45" x2="100" y2="-14"/>
    <line class="corner-line" x1="681" y1="45" x2="740" y2="-14"/>
    <line class="corner-line" x1="159" y1="795" x2="100" y2="854"/>
    <line class="corner-line" x1="681" y1="795" x2="740" y2="854"/>

    <g role="img" aria-label="Looped corner flourishes">
      <circle class="corner-ornament" cx="92" cy="-22" r="12" transform="translate(0 70)"/>
      <circle class="corner-ornament" cx="748" cy="48" r="12"/>
      <circle class="corner-ornament" cx="92" cy="792" r="12"/>
      <circle class="corner-ornament" cx="748" cy="792" r="12"/>
    </g>

    <!-- farm name -->
    <text class="farm-name" x="420" y="180" text-anchor="middle">QUIET HERON FARM</text>

    <!-- oval illustration area -->
    <ellipse class="illustration-area" cx="420" cy="360" rx="240" ry="150"
             role="img" aria-label="Line illustration of a farmhouse with the farm's two dogs in front"/>

    <text class="est-label" x="168" y="372" text-anchor="end">EST</text>
    <text class="est-label" x="672" y="372" text-anchor="start">2021</text>

    <text class="town-label" x="420" y="565" text-anchor="middle">MARROWFIELD, MI</text>

    <text class="address-line" x="420" y="680" text-anchor="middle">27841 BRAVENFIELD ROAD</text>
  </g>

  <!-- height dimension -->
  <g class="dimension dimension-height">
    <path class="dimension-line" d="M1025 150 H1075 V990 H1025"/>
    <rect x="1060" y="535" width="30" height="70" fill="var(--paper)"/>
    <text class="dimension-label" transform="translate(1086 570) rotate(-90)" text-anchor="middle">1m</text>
  </g>

  <!-- width dimension -->
  <g class="dimension dimension-width">
    <path class="dimension-line" d="M150 1000 V1080 H990 V1000"/>
    <rect x="535" y="1062" width="70" height="36" fill="var(--paper)"/>
    <text class="dimension-label" x="570" y="1090" text-anchor="middle">1m</text>
  </g>
</svg>
</body>
</html>
```